Flyer Design

We are a property company and need attractive flyers that will grab peoples attention. We want them to be bold but simple and not too busy. I attach a draft and also our logo. We will print in A5 size.
Thank you & I look forward to receiving designs.

Industry/Entity Type

It Company

```html
<!DOCTYPE html>
<html lang="en">
<head>
<meta charset="utf-8">
<title>Kora Developments – Subdivision Flyer</title>
<link href="https://fonts.googleapis.com/css2?family=Saira+Semi+Condensed:wght@700&family=Saira+Condensed:wght@500&family=Open+Sans:wght@400&display=swap" rel="stylesheet">
<style>
  :root {
    --page-bg: #ebeaea;
    --navy-deep: #2c4068;
    --navy-mid: #5c7499;
    --haze: #c9d3df;
    --paper: #eef1f5;
    --ribbon-blue: #253f8e;
    --band-red: #d4232b;
    --band-orange: #d9714f;
    --contact-brown: #7a5229;
    --white: #ffffff;
  }
  * { box-sizing: border-box; margin: 0; padding: 0; }
  html, body { width: 1200px; height: 1200px; overflow: hidden; background: var(--page-bg); }
  .flyer {
    position: absolute; left: 210px; top: 50px;
    width: 780px; height: 1100px; overflow: hidden;
    box-shadow: 0 6px 24px rgba(0,0,0,.18);
  }
  .flyer__photo {
    position: absolute; inset: 0;
    background:
      linear-gradient(180deg, rgba(0,0,0,0) 78%, rgba(30,45,80,.55) 86%, rgba(0,0,0,0) 94%),
      linear-gradient(170deg, var(--navy-deep) 0%, var(--navy-mid) 22%, var(--haze) 42%, var(--paper) 58%, #dfe6ee 100%);
  }
  .headline {
    position: absolute; left: 40px; right: 40px; top: 100px;
    font-family: "Saira Semi Condensed", sans-serif; font-weight: 700;
    font-variant: small-caps; color: var(--white);
    text-align: center; font-size: 50px; line-height: 50px; letter-spacing: 2px;
    text-shadow: 2px 3px 5px rgba(0,0,0,.45);
  }
  .headline p + p { margin-top: 40px; }
  .offer-band {
    position: absolute; left: 0; right: 0; top: 612px; height: 106px;
    background: linear-gradient(90deg, var(--band-orange) 0%, var(--band-red) 48%, var(--band-red) 100%);
  }
  .offer-band__text {
    position: absolute; right: 36px; top: 14px; width: 380px;
    font-family: "Saira Semi Condensed", sans-serif; font-weight: 700;
    font-variant: small-caps; color: var(--white);
    text-align: right; font-size: 29px; line-height: 27px; letter-spacing: 1px;
  }
  .ribbon {
    position: absolute; left: 48px; top: 540px; width: 268px; height: 560px;
  }
  .ribbon svg { position: absolute; inset: 0; }
  .ribbon__text {
    position: absolute; left: 0; right: 0; top: 84px;
    font-family: "Saira Condensed", sans-serif; font-weight: 500;
    color: var(--white); text-transform: uppercase;
    text-align: center; font-size: 44px; line-height: 50px;
  }
  .brand {
    position: absolute; left: 0; right: 0; bottom: 28px;
    display: flex; flex-direction: column; align-items: center; gap: 14px;
    color: var(--white);
    font-family: "Saira Condensed", sans-serif; font-weight: 500;
    font-size: 28px; line-height: 34px; letter-spacing: 1px;
  }
  .brand__mark { width: 52px; height: 52px; background: var(--white); }
  .contact {
    position: absolute; right: 0; top: 970px; width: 320px; height: 100px;
    background: var(--contact-brown); color: var(--white);
    font-family: "Open Sans", sans-serif; font-size: 19px; line-height: 28px;
    padding: 8px 0 0 16px;
  }
  .contact__row { display: flex; align-items: center; gap: 8px; }
  .contact__row svg { width: 16px; height: 16px; flex: none; }
</style>
</head>
<body>
  <article class="flyer">
    <div class="flyer__photo" role="img" aria-label="Blurred close-up of financial statements with a pen, in blue tones"></div>

    <div class="headline">
      <p>Are you a homeowner<br>looking for financial<br>freedom while been able<br>to keep your own home?</p>
      <p>Are you struggling<br>to pay your mortgage?</p>
    </div>

    <div class="offer-band">
      <p class="offer-band__text">Find out if your property is suitable for subdivision in Auckland</p>
    </div>

    <div class="ribbon">
      <svg viewBox="0 0 268 560" preserveAspectRatio="none" aria-hidden="true">
        <polygon points="0,0 134,60 268,0 268,560 0,560" fill="var(--ribbon-blue)"/>
      </svg>
      <p class="ribbon__text">Kora<br>specialise in<br>subdivisions<br>including<br>finance and<br>management.</p>
      <div class="brand">
        <span class="brand__mark" aria-hidden="true"></span>
        <span class="brand__name">Kora Developments</span>
      </div>
    </div>

    <div class="contact">
      <p class="contact__row">
        <svg viewBox="0 0 16 16" aria-hidden="true"><path d="M3 1h3l1 4-2 1a9 9 0 0 0 5 5l1-2 4 1v3c0 1-1 2-2 2A13 13 0 0 1 1 3c0-1 1-2 2-2z" fill="#fff"/></svg>
        021 555 014
      </p>
      <p class="contact__row">
        <svg viewBox="0 0 16 16" aria-hidden="true"><rect x="1" y="3" width="14" height="10" fill="none" stroke="#fff" stroke-width="1.6"/><path d="M1 3l7 6 7-6" fill="none" stroke="#fff" stroke-width="1.6"/></svg>
        info@korasubdivisions.com
      </p>
      <p class="contact__row">
        <svg viewBox="0 0 16 16" aria-hidden="true"><circle cx="8" cy="8" r="6.5" fill="none" stroke="#fff" stroke-width="1.4"/><ellipse cx="8" cy="8" rx="3" ry="6.5" fill="none" stroke="#fff" stroke-width="1.2"/><path d="M1.5 8h13" stroke="#fff" stroke-width="1.2"/></svg>
        www.korasubdivisions.com
      </p>
    </div>
  </article>
</body>
</html>
```